Web Design for a recruitment company

Website is for a recruitment company, with a particular focus on temporary staff, trades, skilled, and unskilled labour markets. Website will consist of a home page design and separate design for additional pages. Website will be implemented as a template in SharePoint. There is a separate design project for a new logo and look colours will need to be co-ordinated.

Target Market(s)

Company executives in the construction and trades areas looking for staff. Trades people, skilled and unskilled labourers looking for work.

Industry/Entity Type

It Company

Number of Pages Required

2 page

Requirements
Must have
• Looking for Home Page design plus design for additional pages.
• .
Nice to have
• Good Crew | Good Site is the firms byline, company name is TOV Staffing. They will be in the Logo (separate project) but may also appear elsewhere in the design.
• Company values (attached file) may be reflected in the design where practical.

```html
<!DOCTYPE html>
<html lang="en">
<head>
<meta charset="utf-8">
<title>TOV Staffing – Good Crew | Good Site</title>
<link href="https://fonts.googleapis.com/css2?family=Noticia+Text:wght@400;700&family=Open+Sans:ital,wght@0,300;0,400;0,600;1,400&display=swap" rel="stylesheet">
<style>
:root{
  --blue:#0aa3e2;
  --blue-dark:#0890c9;
  --ink:#3a3a3a;
  --muted:#8a8a8a;
  --line:#e1e1e1;
  --field:#eeeeee;
  --band:#f2f2f2;
  --footer:#383838;
  --footer-base:#262626;
  --orange:#f0913a;
  --green:#1fbf6a;
  --white:#ffffff;
}
*{box-sizing:border-box;margin:0;padding:0}
html,body{width:742px;height:1200px;overflow:hidden;background:var(--white)}
body{position:relative;font-family:'Open Sans',sans-serif;color:var(--ink)}
.abs{position:absolute}
.serif{font-family:'Noticia Text',serif}

/* hero */
.hero{position:absolute;left:0;top:0;width:742px;height:326px;
  background:linear-gradient(100deg,#3b3a36 0%,#6d6458 35%,#8a7f70 55%,#4a4742 80%,#2c2c2c 100%)}
.hero::after{content:"";position:absolute;inset:0;background:rgba(20,22,26,.45)}
.site-header{position:absolute;left:0;top:0;width:742px;height:57px;border-bottom:1px solid rgba(255,255,255,.18);z-index:2}
.brand{position:absolute;left:99px;top:13px;display:flex;align-items:flex-start;gap:10px;color:var(--white)}
.brand-dot{width:26px;height:26px;border-radius:50%;background:var(--white);margin-top:2px}
.brand-name{font-family:'Noticia Text',serif;font-weight:700;font-size:20px;line-height:22px}
.brand-byline{font-size:9.5px;line-height:13px;opacity:.9}
.nav{position:absolute;left:303px;top:19px;display:flex;font-family:'Noticia Text',serif;font-size:8.5px;color:var(--white)}
.nav a{color:inherit;text-decoration:none;padding:6px 10px;height:21px}
.nav a.active{background:rgba(30,30,30,.75)}
.login{position:absolute;left:649px;top:15px;width:93px;height:28px;background:var(--blue);color:var(--white);
  font-size:10px;font-weight:600;display:flex;align-items:center;justify-content:center;padding-left:10px;
  clip-path:polygon(10px 0,100% 0,100% 100%,10px 100%,0 50%)}
.hero-title{position:absolute;left:0;width:742px;top:118px;display:flex;justify-content:center;align-items:center;gap:14px;
  color:var(--white);font-weight:600;font-size:27px;letter-spacing:.5px;z-index:2}
.hero-title .dot{width:24px;height:24px;border-radius:50%;background:var(--blue)}
.hero-title .sep{width:1px;height:26px;background:rgba(255,255,255,.4);margin:0 8px}
.hero-copy{position:absolute;left:0;width:742px;top:166px;text-align:center;color:var(--white);
  font-family:'Noticia Text',serif;font-size:13.5px;line-height:18px;z-index:2}
.search{position:absolute;left:99px;top:221px;width:544px;height:33px;border:1px solid rgba(255,255,255,.3);z-index:2}
.search .f{position:absolute;top:6px;height:20px;background:var(--white);font-size:8px;font-style:italic;color:#777;padding:5px 9px}
.search .sel::after{content:"";position:absolute;right:7px;top:6px;border:3px solid transparent;border-bottom-color:var(--blue);border-top:0;}
.search .sel::before{content:"";position:absolute;right:7px;top:11px;border:3px solid transparent;border-top-color:var(--blue);border-bottom:0}
.search .btn{position:absolute;left:449px;top:6px;width:89px;height:20px;background:var(--blue);color:var(--white);
  font-size:8.5px;font-weight:600;display:flex;align-items:center;justify-content:center}

/* partner strip */
.partners{position:absolute;left:0;top:326px;width:742px;height:51px;border-bottom:1px solid var(--line);
  display:flex;justify-content:center;align-items:center;gap:0}
.partners span{width:58px;text-align:center;font-size:13px;font-weight:600;color:#a9a9a9}

/* jobs */
.section-title{font-family:'Noticia Text',serif;color:var(--blue);font-size:18px;text-align:center}
.jobs{position:absolute;left:99px;top:439px;width:361px;border:1px solid var(--line)}
.job{position:relative;height:36.6px;border-bottom:1px solid var(--line)}
.job:last-child{border-bottom:0}
.job .mark{position:absolute;left:14px;top:10px;width:16px;height:16px;border-radius:2px}
.job .title{position:absolute;left:39px;top:8px;font-size:9px;line-height:11px;color:#333}
.job .title small{display:block;font-size:6.5px;color:var(--muted)}
.job .div1,.job .div2{position:absolute;top:0;width:1px;height:100%;background:var(--line)}
.job .div1{left:169px}.job .div2{left:280px}
.job .pin{position:absolute;left:189px;top:12px}
.job .city{position:absolute;left:202px;top:13px;font-size:7.5px}
.job .tag{position:absolute;left:291px;top:11px;width:58px;height:14px;color:var(--white);font-size:6.5px;font-weight:600;
  display:flex;align-items:center;justify-content:center}
.full{background:var(--blue)}.part{background:var(--orange)}.free{background:var(--green)}
.more{position:absolute;left:99px;top:630px;width:361px;height:20px;background:var(--blue);border-bottom:2px solid var(--blue-dark);
  color:var(--white);font-size:7.5px;font-weight:600;display:flex;align-items:center;justify-content:center}

.callback{position:absolute;left:476px;top:410px;width:167px;height:212px;border:1px solid var(--line)}
.callback h3{position:absolute;left:40px;top:10px;font-family:'Noticia Text',serif;font-weight:400;color:var(--blue);font-size:11.5px}
.callback .ico{position:absolute;left:13px;top:9px}
.callback hr{position:absolute;left:13px;top:32px;width:141px;border:0;border-top:1px solid var(--line)}
.callback p{position:absolute;left:13px;top:43px;width:145px;font-size:6.5px;line-height:8.5px;color:#666}
.callback .in{position:absolute;left:13px;width:141px;height:18px;background:var(--field);font-size:6.5px;font-style:italic;color:#888;padding:5px 9px}
.callback .in.sel::after{content:"";position:absolute;right:8px;top:8px;border:3px solid transparent;border-top-color:#999;border-bottom:0}
.callback .go{position:absolute;left:13px;top:176px;width:141px;height:23px;background:var(--blue);color:var(--white);
  font-size:8.5px;font-weight:600;display:flex;align-items:center;justify-content:center}

/* stats */
.stats{position:absolute;left:0;top:685px;width:742px;height:205px;background:var(--band)}
.stats .lead{position:absolute;left:0;width:742px;top:58px;text-align:center;font-size:9px;line-height:12px;color:#555}
.stat{position:absolute;top:118px;width:96px;text-align:center}
.stat b{display:block;font-weight:300;font-size:20px;line-height:24px;color:#555}
.stat span{font-size:9px;color:#777}
.vsep{position:absolute;top:112px;width:1px;height:53px;background:#dcdcdc}

/* register */
.register{position:absolute;left:0;top:890px;width:742px;height:153px;background:var(--blue);color:var(--white);text-align:center}
.register h2{position:absolute;left:0;width:742px;top:30px;font-family:'Noticia Text',serif;font-weight:400;font-size:17px}
.register p{position:absolute;left:100px;width:542px;top:58px;font-size:9px;line-height:12px}
.register .cta{position:absolute;left:322px;top:95px;width:99px;height:21px;background:var(--white);color:#555;
  font-size:7.5px;font-weight:600;display:flex;align-items:center;justify-content:center}

/* footer */
.footer{position:absolute;left:0;top:1043px;width:742px;height:109px;background:var(--footer);color:var(--white)}
.fcol{position:absolute;top:30px;width:127px;text-align:center}
.fcol h4{font-family:'Noticia Text',serif;font-weight:400;font-size:9.5px;padding-bottom:8px;border-bottom:2px solid #2b2b2b}
.fcol div{font-size:8px;line-height:10.5px;margin-top:9px}
.base{position:absolute;left:0;top:1152px;width:742px;height:48px;background:var(--footer-base)}
.base .dot{position:absolute;left:357px;top:10px;width:28px;height:28px;border-radius:50%;background:var(--blue)}
</style>
</head>
<body>

<section class="hero" role="img" aria-label="Photo of a student reading a book at a library desk"></section>

<header class="site-header">
  <div class="brand">
    <div class="brand-dot"></div>
    <div>
      <div class="brand-name">TOV Staffing</div>
      <div class="brand-byline">Good Crew &nbsp;|&nbsp; Good Site</div>
    </div>
  </div>
  <nav class="nav">
    <a class="active">HOME</a><a>ABOUT US</a><a>JOBS</a><a>CANDIDATES</a><a>CONTACT US</a><a>BLOG</a>
  </nav>
  <div class="login">LOGIN</div>
</header>

<h1 class="hero-title"><span class="dot"></span>GOOD CREW<span class="sep"></span>GOOD SITE</h1>
<p class="hero-copy">This is Draftwell's version&nbsp; of Lorem Ipsum. Proin gravida nibh vel velit auctor aliquet.<br>Aenean sollicitudin, lorem quis bibendum auctor,</p>

<form class="search">
  <div class="f" style="left:6px;width:164px">Keywords</div>
  <div class="f sel" style="left:174px;width:133px">All Regions</div>
  <div class="f sel" style="left:312px;width:133px">Any Category</div>
  <div class="btn">SEARCH</div>
</form>

<div class="partners">
  <span>Arkon</span><span>Paylo</span><span>Fizzo</span><span>Fortis</span><span>Bidly</span><span>Castell</span><span>Softline</span><span>Zenta</span><span>Astrin</span>
</div>

<h2 class="section-title abs" style="left:99px;width:361px;top:405px">Our Latest Jobs</h2>

<div class="jobs">
  <div class="job"><span class="mark" style="background:#cfe3f3"></span><div class="title">Senior Graphic Designer<small>Design Technology</small></div><i class="div1"></i>
    <svg class="pin" width="8" height="11" viewBox="0 0 8 11"><path d="M4 10.5S.8 6.6.8 4a3.2 3.2 0 016.4 0C7.2 6.6 4 10.5 4 10.5z" fill="none" stroke="#444" stroke-width="1.2"/><circle cx="4" cy="4" r="1.1" fill="#444"/></svg>
    <span class="city">New York</span><i class="div2"></i><span class="tag full">Full-Time</span></div>
  <div class="job"><span class="mark" style="background:#c9d4ea"></span><div class="title">Duty Manager<small>Restaurant Customer Host</small></div><i class="div1"></i>
    <svg class="pin" width="8" height="11" viewBox="0 0 8 11"><path d="M4 10.5S.8 6.6.8 4a3.2 3.2 0 016.4 0C7.2 6.6 4 10.5 4 10.5z" fill="none" stroke="#444" stroke-width="1.2"/><circle cx="4" cy="4" r="1.1" fill="#444"/></svg>
    <span class="city">San Francisco</span><i class="div2"></i><span class="tag part">Part-Time</span></div>
  <div class="job"><span class="mark" style="background:#f0d27a"></span><div class="title">Web Developer<small>Design Technology</small></div><i class="div1"></i>
    <svg class="pin" width="8" height="11" viewBox="0 0 8 11"><path d="M4 10.5S.8 6.6.8 4a3.2 3.2 0 016.4 0C7.2 6.6 4 10.5 4 10.5z" fill="none" stroke="#444" stroke-width="1.2"/><circle cx="4" cy="4" r="1.1" fill="#444"/></svg>
    <span class="city">New York</span><i class="div2"></i><span class="tag full">Full-Time</span></div>
  <div class="job"><span class="mark" style="background:#f08a3c"></span><div class="title">Web Developer<small>Design Technology</small></div><i class="div1"></i>
    <svg class="pin" width="8" height="11" viewBox="0 0 8 11"><path d="M4 10.5S.8 6.6.8 4a3.2 3.2 0 016.4 0C7.2 6.6 4 10.5 4 10.5z" fill="none" stroke="#444" stroke-width="1.2"/><circle cx="4" cy="4" r="1.1" fill="#444"/></svg>
    <span class="city">London</span><i class="div2"></i><span class="tag full">Full-Time</span></div>
  <div class="job"><span class="mark" style="background:#d3d9ea"></span><div class="title">Senior Graphic Designer<small>Design Technology</small></div><i class="div1"></i>
    <svg class="pin" width="8" height="11" viewBox="0 0 8 11"><path d="M4 10.5S.8 6.6.8 4a3.2 3.2 0 016.4 0C7.2 6.6 4 10.5 4 10.5z" fill="none" stroke="#444" stroke-width="1.2"/><circle cx="4" cy="4" r="1.1" fill="#444"/></svg>
    <span class="city">Miami</span><i class="div2"></i><span class="tag free">Freelance</span></div>
</div>
<div class="more">+ LOAD MORE LISTINGS</div>

<aside class="callback">
  <svg class="ico" width="22" height="20" viewBox="0 0 22 20"><circle cx="11" cy="10" r="7" fill="none" stroke="#444" stroke-width="1.4"/><path d="M3 10a8 8 0 0116 0" fill="none" stroke="#444" stroke-width="1.4"/><rect x="1.5" y="8" width="3" height="5" rx="1" fill="#444"/><rect x="17.5" y="8" width="3" height="5" rx="1" fill="#444"/><circle cx="8.5" cy="9" r=".9" fill="#444"/><circle cx="13.5" cy="9" r=".9" fill="#444"/><path d="M8.5 12.5q2.5 2 5 0" fill="none" stroke="#444"/></svg>
  <h3>Request a Call Back</h3>
  <hr>
  <p>This is Draftwell's version&nbsp; of Lorem Ipsum. Proin gravida nibh vel velit</p>
  <div class="in" style="top:71px">Name</div>
  <div class="in" style="top:96px">Email</div>
  <div class="in" style="top:122px">Phone Number</div>
  <div class="in sel" style="top:147px">I'm a...... please select</div>
  <div class="go">Call Me Back</div>
</aside>

<section class="stats">
  <h2 class="section-title abs" style="left:0;width:742px;top:29px">TOV Staffing Site Stats</h2>
  <p class="lead">Here we list our site stats and how many people we've helped find a job and companies have found recruits.<br>It's a pretty awesome stats area!</p>
  <div class="stat" style="left:131px"><b>44</b><span>Jobs Posted</span></div>
  <i class="vsep" style="left:227px"></i>
  <div class="stat" style="left:227px"><b>50</b><span>Resumes Posted</span></div>
  <i class="vsep" style="left:323px"></i>
  <div class="stat" style="left:323px"><b>104</b><span>Jobs Filled</span></div>
  <i class="vsep" style="left:419px"></i>
  <div class="stat" style="left:418px"><b>91</b><span>Companies</span></div>
  <i class="vsep" style="left:515px"></i>
  <div class="stat" style="left:515px"><b>2,152</b><span>Members</span></div>
</section>

<section class="register">
  <h2>Register as a Candidate Now !</h2>
  <p>This is Draftwell's version&nbsp; of Lorem Ipsum. Proin gravida nibh vel velit auctor aliquet. Aenean sollicitudin, lorem quis bibendum auctor, nisi elit consequat ipsum, nec sagittis sem nibh id elit.</p>
  <div class="cta">REGISTER NOW</div>
</section>

<footer class="footer">
  <div class="fcol" style="left:99px"><h4>Call</h4><div>1800-555-017</div></div>
  <div class="fcol" style="left:237px"><h4>Email</h4><div>info@tovstaffing.com</div></div>
  <div class="fcol" style="left:376px"><h4>Follow</h4><div>Chatterly | Pingr | Feedline</div></div>
  <div class="fcol" style="left:515px"><h4>Visit</h4><div>42, Lane No: 15,<br>Dolor Sit Amet Plaza 210/07</div></div>
</footer>
<div class="base"><span class="dot"></span></div>

</body>
</html>
```